Beer bottle label / Tap badge

What: Graphics to be used on both a beer tap badge and a beer bottle label
Requirements:
• Represent a differentiated quality product
• Include brewery name and logo for brand recognition
• Include and represent the Name “Idle Harbor”
• Include the beer style “American Cream Ale”
• A format that can be used both in a circular tap badge and a square / rectangular bottle label
At Merry Anchor Brewing Co. we design and brew quality beers across a range of styles. We use traditional ingredients and techniques to produce brews for you that are bursting with flavor and easy to drink. Our passion and commitment to excellence are captured in every bottle. Give them a try and see what we mean.
Idle Harbor
American Cream Ale
An easy drinking session beer that won’t make you work to enjoy it. This is crafted to be smooth with a modicum of honey toasted oats and a yeast strain that leaves a fruity, very light, soft balanced palate. Perfectly hopped for a balanced experience this beer is made for you.
Updates
Thanks to everyone who submitted a design. My apologies for not providing any feedback over the past few days since we took a short break over Christmas. We've extended the deadline by a few days and we'll be in touch shortly.
Industry/Entity Type
Brewery
Requirements
Must have
- - Include brewery name and logo for brand recognition
- Include and represent the Name “Idle Harbor”
- Include the beer style “American Cream Ale”
- include volume (330ml) and % alcohol (4.5% alcohol)
Nice to have
- Idle Harbor is a very drinkable, smooth and easy beer that is perfect for a sunny lazy afternoon. We would like the graphic to represent the beer. So, perhaps a friendly (smiling) skeleton on a hammock or on the beach enjoying life .....

```html
<!DOCTYPE html>
<html lang="en">
<head>
<meta charset="utf-8">
<title>Idle Harbor – American Cream Ale Label</title>
<link rel="stylesheet" href="https://fonts.googleapis.com/css2?family=Alfa+Slab+One&family=Lobster&family=Libre+Baskerville:wght@400;700&display=swap">
<style>
  :root {
    --stage: #1f1f1f;
    --orange-hot: #f25a1c;
    --orange: #e0441a;
    --orange-deep: #b52d12;
    --cream: #f8e6d2;
    --cream-soft: rgba(248, 230, 210, 0.55);
    --maroon: #6e0f12;
    --maroon-dark: #4a080b;
    --ink: #2a0a0a;
  }
  * { box-sizing: border-box; margin: 0; padding: 0; }
  html, body {
    width: 1200px; height: 1017px; overflow: hidden;
    background: var(--stage);
  }
  .canvas {
    position: relative; width: 1200px; height: 1017px;
  }
  .bottle-label {
    position: absolute; left: 260px; top: 50px;
    width: 680px; height: 917px;
    background: radial-gradient(ellipse at 50% 35%, var(--orange-hot) 0%, var(--orange) 55%, var(--orange-deep) 100%);
    border-radius: 0 0 50% 50% / 0 0 16% 16%;
    text-align: center;
    color: var(--cream);
  }
  .ornament {
    position: absolute; background: var(--cream-soft); border-radius: 40px;
  }
  .ornament--top-swirl { left: 230px; top: 40px; width: 220px; height: 36px; }
  .ornament--wheat-left { left: 60px; top: 150px; width: 60px; height: 26px; transform: rotate(-25deg); }
  .ornament--wheat-right { right: 60px; top: 150px; width: 60px; height: 26px; transform: rotate(25deg); }
  .ornament--bottom-swirl { left: 200px; top: 408px; width: 240px; height: 30px; }
  .ornament--wheat-under { left: 280px; top: 702px; width: 120px; height: 18px; }

  .beer-name {
    position: absolute; left: 0; right: 0; top: 88px;
    font-family: "Alfa Slab One", serif;
    font-weight: 400;
    line-height: 1.06;
    letter-spacing: 4px;
    color: var(--cream);
    text-shadow: 3px 3px 0 var(--maroon), 6px 6px 0 var(--maroon), 9px 9px 0 var(--maroon-dark);
  }
  .beer-name__line { display: block; }
  .beer-name__line--first { font-size: 128px; }
  .beer-name__line--second { font-size: 120px; }

  .brewery-mark {
    position: absolute; right: 34px; top: 446px;
    display: flex; align-items: center; gap: 10px;
  }
  .brewery-mark__dot {
    width: 40px; height: 40px; border-radius: 50%; background: var(--ink);
  }
  .brewery-mark__name {
    font-family: "Libre Baskerville", serif; font-weight: 700;
    font-size: 15px; line-height: 1.25; color: var(--ink); text-align: left;
    width: 120px;
  }

  .style-ribbon {
    position: absolute; left: 30px; top: 548px; width: 620px; height: 130px;
  }
  .style-ribbon svg { position: absolute; inset: 0; }
  .style-ribbon__title {
    position: absolute; left: 0; right: 0; top: 14px;
    font-family: "Lobster", cursive; font-size: 46px; color: var(--cream);
  }
  .style-ribbon__tagline {
    position: absolute; left: 0; right: 0; top: 74px;
    font-family: "Libre Baskerville", serif; font-size: 15px; color: var(--cream);
  }
  .volume {
    position: absolute; left: 0; right: 0; top: 772px;
    font-family: "Libre Baskerville", serif; font-size: 30px; color: var(--cream);
  }
</style>
</head>
<body>
<main class="canvas">
  <section class="bottle-label">
    <div class="ornament ornament--top-swirl" role="img" aria-label="Decorative swirl flourish"></div>
    <div class="ornament ornament--wheat-left" role="img" aria-label="Wheat sprig ornament"></div>
    <div class="ornament ornament--wheat-right" role="img" aria-label="Wheat sprig ornament"></div>

    <h1 class="beer-name">
      <span class="beer-name__line beer-name__line--first">IDLE</span>
      <span class="beer-name__line beer-name__line--second">HARBOR</span>
    </h1>

    <div class="ornament ornament--bottom-swirl" role="img" aria-label="Decorative swirl flourish"></div>

    <div class="brewery-mark">
      <span class="brewery-mark__name">Merry Anchor Brewing Co.</span>
      <span class="brewery-mark__dot"></span>
    </div>

    <div class="style-ribbon">
      <svg width="620" height="130" viewBox="0 0 620 130" aria-hidden="true">
        <polygon points="0,40 70,40 70,118 0,118 26,79" fill="var(--maroon-dark)"/>
        <polygon points="620,40 550,40 550,118 620,118 594,79" fill="var(--maroon-dark)"/>
        <polygon points="50,100 70,118 70,100" fill="var(--ink)"/>
        <polygon points="570,100 550,118 550,100" fill="var(--ink)"/>
        <rect x="50" y="8" width="520" height="92" fill="var(--maroon)"/>
      </svg>
      <div class="style-ribbon__title">American Cream Ale</div>
      <div class="style-ribbon__tagline">Perfectly hopped for a Balanced experience</div>
    </div>

    <div class="ornament ornament--wheat-under" role="img" aria-label="Wheat ear ornament"></div>

    <p class="volume">4.5% Alc&nbsp; Vol - 330ml</p>
  </section>
</main>
</body>
</html>
```